Business Cards for a law firm

Business cards for our law firm. Use our silhoette logo and OAK HARBOR - check our website (www.oakharbor-legal.com)

Contact Information for Business Card

our silhouette logo, OAK HARBOR, 800-555-0147, Dorian Kestrup, dorian@oakharbor-legal.com

Requirements
Must have
• our silhouette logo, OAK HARBOR, 800-555-0147, Dorian Kestrup, dorian@oakharbor-legal.com

```html
<!DOCTYPE html>
<html lang="en">
<head>
<meta charset="utf-8">
<title>Oak Harbor — Business Cards</title>
<link rel="stylesheet" href="https://fonts.googleapis.com/css2?family=Montserrat:wght@400;500;700&display=swap">
<style>
  :root {
    --stage: #3b3b3d;
    --paper: #e9ebee;
    --navy: #1e2a5e;
    --navy-deep: #172250;
    --navy-soft: #2a3a7a;
    --ink-light: #dfe3ea;
  }
  * { box-sizing: border-box; margin: 0; padding: 0; }
  html, body {
    width: 1200px; height: 905px; overflow: hidden;
    background: var(--stage);
    font-family: "Montserrat", sans-serif;
  }
  .stage {
    position: relative; width: 1200px; height: 905px;
    display: flex; flex-direction: column; align-items: center; justify-content: center;
    gap: 56px;
  }
  .card {
    position: relative; width: 560px; height: 320px;
    border-radius: 3px; overflow: hidden;
    box-shadow: 0 14px 30px rgba(0,0,0,.35);
  }
  /* Front */
  .card-front { background: var(--paper); color: var(--navy); }
  .brand-artwork {
    position: absolute; left: 30px; top: 0; width: 240px; height: 320px;
    background: linear-gradient(180deg, var(--navy-soft) 0%, var(--navy) 100%);
  }
  .identity { position: absolute; left: 296px; top: 120px; white-space: nowrap; }
  .identity .person-name {
    font-weight: 700; font-size: 19px; letter-spacing: 1.5px;
  }
  .identity .person-role {
    font-weight: 700; font-size: 10px; margin-top: 3px;
  }
  .contact-list {
    position: absolute; left: 296px; top: 215px;
    list-style: none; font-size: 13px; font-weight: 400;
    letter-spacing: 1px; line-height: 19px; white-space: nowrap;
  }
  /* Back */
  .card-back { background: var(--navy-deep); }
  .brand-lockup {
    position: absolute; left: 50%; top: 50%;
    transform: translate(-50%, -50%);
    display: flex; align-items: center; gap: 14px;
    color: var(--ink-light);
  }
  .brand-mark { width: 22px; height: 22px; background: var(--ink-light); }
  .brand-name {
    font-weight: 500; font-size: 28px; letter-spacing: 4px; white-space: nowrap;
  }
</style>
</head>
<body>
<main class="stage">
  <section class="card card-front" aria-label="Business card front">
    <div class="brand-artwork" role="img" aria-label="Brand silhouette artwork area"></div>
    <div class="identity">
      <p class="person-name">Dorian Kestrup</p>
      <p class="person-role">Attorney at Law</p>
    </div>
    <ul class="contact-list">
      <li>800-555-0147</li>
      <li>dorian@oakharbor-legal.com</li>
      <li>www.oakharbor-legal.com</li>
    </ul>
  </section>

  <section class="card card-back" aria-label="Business card back">
    <div class="brand-lockup">
      <span class="brand-mark" aria-hidden="true"></span>
      <span class="brand-name">OAK HARBOR</span>
    </div>
  </section>
</main>
</body>
</html>
```